Newspaper print advert for medical clinic business - The Harbourline Clinic

I need a new advert to go into a local print newspaper. The business is a medical clinic looking after tourists, residents and expats living in Mallorca, Balearic Islands, Spain. They are 95% British and the advert must include a British theme without being 'Brexit' similar. Professional and high quality tone with a proud British flavor.
The newspaper is the Island Morning Courier. www.islandmorningcourier.com/ It has print and online versions. This advert is for the PRINT version.
Needs to be 200 dpi minimum please. 64 mm high and 82 mm wide.
Art work examples included below but you can reuse the logo design if you like. Make sure logo does not pixelate. I don't have anything more high res...
Example of the tone I am looking for in terms of modern feel = www.theharbourline.clinic
Target Market(s)
Private medical patients including island residents, expatriates and tourists to our 6 existing clinics in Mallorca. The clientele are a mix of British people living on the island for many years with families and UK Tourists who visit the island for a week or two in the summer.
Industry/Entity Type
Healthcare
Font styles to use
Other font styles liked:
- Montserrat
Requirements
Must have
- Must mention: English speaking doctors. British Healthcare in Mallorca since 2001. 5 locations including Portals Nous, Palmanova, Torrenova, Calle Vento Magaluf, Cami Sa Tordera Magaluf,
- www.theharbourline.clinic
- Yacht, Home, Hotel visits on request.
- High quality healthcare from experienced doctors.
- Consultations in English, Spanish or French
- Phone to discuss an appointment (+34) 971 48 27 69
Nice to have
- Under the new ownership from April 2019. (Small print)
Should not have
- No brash promises of recovery or 'trust the doctor'.

```html
<!DOCTYPE html>
<html lang="en">
<head>
<meta charset="utf-8">
<title>The Harbourline Clinic – Newspaper Advert</title>
<link rel="stylesheet" href="https://fonts.googleapis.com/css2?family=Montserrat:wght@400;500;700&display=swap">
<style>
  :root {
    --clinic-red: #d11f3a;
    --clinic-navy: #283779;
    --paper: #ffffff;
    --photo-light: #eef1f3;
    --photo-mid: #dfe5e8;
    --backdrop: #e6e6e6;
  }
  * { margin: 0; padding: 0; box-sizing: border-box; }
  html, body {
    width: 1200px; height: 1200px; overflow: hidden;
    background: var(--backdrop);
    font-family: "Montserrat", Arial, sans-serif;
  }
  .advert {
    position: absolute; left: 30px; top: 156px;
    width: 1140px; height: 888px;
    background: var(--paper); overflow: hidden;
  }
  .advert__shapes { position: absolute; inset: 0; }
  .advert__text { position: absolute; white-space: nowrap; line-height: 1; }
  .tagline { right: 47px; top: 44px; font-size: 25px; font-weight: 500; color: var(--clinic-navy); }
  .brand-name { left: 78px; top: 110px; font-size: 46px; font-weight: 500; color: var(--clinic-navy); }
  .headline-kicker { left: 66px; top: 312px; font-size: 20px; font-weight: 700; color: var(--paper); }
  .headline-main { left: 62px; top: 344px; font-weight: 700; color: var(--paper); }
  .headline-main span { display: block; }
  .headline-main .line-one { font-size: 52px; }
  .headline-main .line-two { font-size: 68px; margin-top: 2px; }
  .languages { left: 66px; top: 490px; font-size: 29px; color: var(--paper); line-height: 1.25; }
  .languages strong { font-weight: 700; display: block; }
  .visits { left: 67px; top: 585px; font-size: 21px; font-weight: 700; color: var(--paper); }
  .locations-title { left: 66px; top: 711px; font-size: 23px; font-weight: 700; color: var(--paper); display: flex; align-items: center; gap: 10px; }
  .locations-list { left: 66px; top: 752px; font-size: 18.5px; color: var(--paper); line-height: 1.4; }
  .appointment { left: 66px; top: 827px; font-size: 32px; font-weight: 700; color: var(--paper); word-spacing: 2px; }
  .website { right: 55px; top: 835px; font-size: 24px; font-weight: 500; color: var(--paper); }
</style>
</head>
<body>
  <section class="advert" aria-label="The Harbourline Clinic advert">
    <svg class="advert__shapes" width="1140" height="888" viewBox="0 0 1140 888">
      <defs>
        <radialGradient id="photo-tone" cx="0.55" cy="0.4" r="0.7">
          <stop offset="0" stop-color="var(--photo-light)"/>
          <stop offset="1" stop-color="var(--photo-mid)"/>
        </radialGradient>
      </defs>
      <path class="red-band" fill="var(--clinic-red)"
        d="M0 190 C120 245 230 265 330 250 C520 220 680 110 860 100 C980 95 1080 125 1140 155 L1140 888 L0 888 Z"/>
      <circle class="photo-area" cx="862" cy="480" r="368" fill="url(#photo-tone)"
        role="img" aria-label="Photograph of a smiling doctor in a white coat with a stethoscope, holding a tablet"/>
      <path class="navy-band" fill="var(--clinic-navy)"
        d="M0 722 C110 670 220 640 320 645 C450 652 540 720 650 760 C760 798 900 805 1000 780 C1060 765 1110 745 1140 725 L1140 888 L0 888 Z"/>
    </svg>

    <p class="advert__text tagline">British Healthcare in Mallorca since 2001.</p>
    <p class="advert__text brand-name">The Harbourline Clinic</p>

    <p class="advert__text headline-kicker">HIGH QUALITY HEALTHCARE FROM</p>
    <h1 class="advert__text headline-main">
      <span class="line-one">EXPERIENCED</span>
      <span class="line-two">DOCTORS.</span>
    </h1>
    <p class="advert__text languages">Consultations in<strong>English, Spanish or French</strong></p>
    <p class="advert__text visits">Yacht, Home, Hotel visits on request</p>

    <p class="advert__text locations-title">
      <svg width="16" height="22" viewBox="0 0 16 22" aria-hidden="true">
        <circle cx="8" cy="6.5" r="4.5" fill="none" stroke="var(--paper)" stroke-width="2"/>
        <path d="M8 11 L8 17" stroke="var(--paper)" stroke-width="2"/>
        <ellipse cx="8" cy="18.5" rx="6" ry="2" fill="none" stroke="var(--paper)" stroke-width="1.6"/>
      </svg>
      5 locations including
    </p>
    <p class="advert__text locations-list">Portals Nous, Palmanova, Torrenova,<br>Calle Vento Magaluf, Cami Sa Tordera Magaluf,</p>

    <p class="advert__text appointment">For appointment&nbsp; (+34) 971 48 27 69</p>
    <p class="advert__text website">www.theharbourline.clinic</p>
  </section>
</body>
</html>
```